Bref créative
Business cards/ Stationary for new travel agency
Stationary & business cards
Bright & Fun-filled
Marla & Ted Kinsolving
Fernhollow, ST
marla@wanderpineharbortours.example
wanderpineharbortours.example

```html
<!DOCTYPE html>
<html lang="en">
<head>
<meta charset="utf-8">
<title>WanderPineHarbor – Business Card</title>
<link href="https://fonts.googleapis.com/css2?family=Cinzel:wght@400;600&display=swap" rel="stylesheet">
<style>
  :root{
    --bg:#e6e7e9;
    --navy:#1c4c9a;
    --navy-deep:#143b7d;
    --royal:#2b62b8;
    --green:#5aa745;
    --ink:#24508f;
    --white:#ffffff;
  }
  *{box-sizing:border-box;margin:0;padding:0}
  html,body{width:1200px;height:895px;overflow:hidden;background:var(--bg)}
  body{font-family:"Cinzel",Georgia,serif;position:relative}

  .card{position:absolute;top:293px;width:540px;height:309px;box-shadow:0 10px 24px rgba(0,0,0,.18)}

  /* Front */
  .card-front{left:40px;background:var(--white);border:11px solid var(--navy);color:var(--ink)}
  .brand{position:absolute;top:40px;left:0;right:0;display:flex;align-items:center;justify-content:center;gap:14px}
  .brand-mark{width:34px;height:34px;border-radius:50%;background:var(--green);flex:none}
  .brand-name{font-size:29px;font-weight:400;color:var(--navy);letter-spacing:.5px;white-space:nowrap}
  .rule{position:absolute;top:100px;left:92px;right:92px;height:2px;background:var(--navy)}
  .owners{position:absolute;top:114px;left:0;right:0;text-align:center;font-size:19px;letter-spacing:1px;color:var(--ink);white-space:nowrap}
  .details{position:absolute;top:168px;left:30px;right:20px;display:flex;align-items:flex-start}
  .location{width:160px;text-align:right;padding-right:16px;padding-top:4px;font-size:11px;letter-spacing:1px;white-space:nowrap}
  .divider{width:1.5px;height:96px;background:var(--navy);flex:none}
  .contacts{list-style:none;padding-left:14px;font-size:10.5px;letter-spacing:.4px;white-space:nowrap}
  .contacts li{display:flex;align-items:center;gap:8px;height:22px}
  .icon{width:15px;height:15px;border-radius:50%;background:var(--navy);display:flex;align-items:center;justify-content:center;flex:none}
  .icon.alt{background:var(--green)}
  .icon svg{width:9px;height:9px}

  /* Back */
  .card-back{left:620px;border:7px solid var(--green);background:radial-gradient(ellipse at 60% 40%,var(--royal) 0%,var(--navy) 55%,var(--navy-deep) 100%)}
  .back-mark{position:absolute;top:68px;left:50%;margin-left:-48px;width:96px;height:96px;border-radius:50%;background:var(--white)}
  .web{position:absolute;left:30px;right:20px;bottom:38px;color:var(--white);font-size:14px;letter-spacing:2.5px;white-space:nowrap}
</style>
</head>
<body>

<section class="card card-front">
  <div class="brand">
    <span class="brand-mark"></span>
    <span class="brand-name">WanderPineHarbor</span>
  </div>
  <div class="rule"></div>
  <p class="owners">MARLA &amp; TED KINSOLVING</p>
  <div class="details">
    <p class="location">FERNHOLLOW, ST</p>
    <div class="divider"></div>
    <ul class="contacts">
      <li><span class="icon"><svg viewBox="0 0 10 10"><path d="M2 1l2 2-1 1.2c.6 1.2 1.6 2.2 2.8 2.8L7 6l2 2-1.3 1.3C4.5 9 1 5.5.7 2.3z" fill="#fff"/></svg></span>(555) 010-4821</li>
      <li><span class="icon alt"><svg viewBox="0 0 10 10"><rect x="2.5" y=".5" width="5" height="9" rx="1" fill="#fff"/></svg></span>(555) 010-7356</li>
      <li><span class="icon"><svg viewBox="0 0 10 10"><rect x="1" y="2.5" width="8" height="5" fill="#fff"/><path d="M1 2.5l4 3 4-3" stroke="#1c4c9a" fill="none" stroke-width=".8"/></svg></span>marla@wanderpineharbortours.example</li>
      <li><span class="icon alt"><svg viewBox="0 0 10 10"><circle cx="5" cy="5" r="3.8" fill="none" stroke="#fff" stroke-width="1"/><path d="M1.2 5h7.6M5 1.2c-2 2.4-2 5.2 0 7.6M5 1.2c2 2.4 2 5.2 0 7.6" stroke="#fff" fill="none" stroke-width=".7"/></svg></span>wanderpineharbortours.example</li>
    </ul>
  </div>
</section>

<section class="card card-back">
  <span class="back-mark"></span>
  <p class="web">WWW.WANDERPINEHARBORTOURS.EXAMPLE</p>
</section>

</body>
</html>
```